7 Herons Distillery - Bottle Label Design

We are a small craft distillery whose branding needs to incorporate our location on a lake (Lac Vernisse, Quebec, Canada). A unique aspect of the lake is that people drive floating docks on the lake powered by a small outboard motor (see photos). Back in the 1970’s when Lac Vernisse was a sparsely populated and difficult-to-access lake in the Gatineau Hills north of Ottawa, the concept of motorized docks was conjured on a lazy afternoon and this single stroke of genius has inadvertently spawned the most exceptional and eccentric lake based community. Throughout the summer, somewhere around four o’clock on any given Friday and Saturday it starts to happen. Docks set sail from their customary landing places - family, friends, snacks and loaded drink coolers in-tow and, as if magnetically drawn, head toward Pine Shoal. Without fail they will come upon a gathering of similar minded floating docks within the vicinity - be guided in with help to moor alongside and within seconds be seamlessly immersed in the festivities. Seldom any longer are these events planned, they have become elemental, a thing organically derived from within the community. This on-going weekly event is the genesis of the strong bond that brings us Seven Herons Distilling.
Each of the 4 distillery owners have one of these docks so hence the name. We are open to either "7 Herons" or spelled out as "Seven Herons" as may be visually appropriate. We are also open to "Distillery" or "Distilling". More detail on the docks themselves, they are 14x16 feet powered by a small outboard motor as shown in the photos. This dock aspect may be difficult to incorporate into the branding but the lake outline is included as an image applicable to include for that local reference aspect. We will be creating very high quality small batch liquors such as vodka, rum, gin and whiskey. Each batch will be triple distilled and perhaps 20 bottles in quantity so very exclusive. We are aiming at a premium feel for the branding. Attached are some bottle label designs that evoke the type of feel we are going for and a photo of the style of blank bottle to design for which is a 750ml Nordic pattern bottle.
In general we are going for more contemporary than traditional, more bold than delicate. If a single label the size desired would be 4 inches wide and 4 inches tall. If a double/split label as in two of the photos the top label would be 3 inches wide and 3 inches tall and the bottom label would be max 4 inches wide and 1.5 inches tall. We are open to the upper label being a "transparent" label to create a printed on bottle effect, perhaps of the brand logo. We are only interested in front label so do not require a back, neck or closure label. The label will require the ability to name the batch style name (example "Tuberix") and then the amplifying information for the type of alcohol (Russian Potato Vodka) in a smaller font. Another example ("Red Fox" and "London Dry Gin"). Information for bottle size (750ml) and alcohol % (40%) are also to be included. Governmental safety warnings are not required. We are open to use of any colours in the label. The basic label design would be re-used for different types of batches where we would change the style and alcohol name.
Updates

Target Market(s)

Up scale premium spirits buyers

Font styles to use
Serif
Sans Serif

Requirements
Must have
• A visual reference to the docks or the lake per the images attached.
Nice to have
• Ideally we can re-use the label design for a different type of Alcohol by changing the alcohol name and style information and maybe the colour of a major element in the label.

```html
<!DOCTYPE html>
<html lang="en">
<head>
<meta charset="utf-8">
<title>Seven Herons Distillery – Tuberix Label</title>
<link rel="stylesheet" href="https://fonts.googleapis.com/css2?family=Barlow:wght@800&family=Montserrat:wght@700&display=swap">
<style>
  :root {
    --page: #f4f4f4;
    --label: #e6e6e6;
    --ink: #111111;
  }
  * { margin: 0; padding: 0; box-sizing: border-box; }
  html, body {
    width: 1200px; height: 848px; overflow: hidden;
    background: var(--page);
  }
  .canvas { position: relative; width: 1200px; height: 848px; }
  .label {
    position: absolute; left: 210px; top: 34px;
    width: 780px; height: 780px;
    background: var(--label); color: var(--ink);
    font-family: "Montserrat", sans-serif; font-weight: 700;
  }
  .brand-name {
    position: absolute; top: 62px; left: 0; width: 100%;
    text-align: center; font-size: 38px; letter-spacing: 2px;
  }
  .brand-rule {
    position: absolute; top: 154px; height: 3px; background: var(--ink);
  }
  .brand-rule.left { left: 36px; width: 235px; }
  .brand-rule.right { right: 36px; width: 235px; }
  .brand-mark {
    position: absolute; left: 362px; top: 128px;
    width: 56px; height: 56px; background: var(--ink);
  }
  .brand-sub {
    position: absolute; top: 216px; left: 0; width: 100%;
    text-align: center; font-size: 25px; letter-spacing: 3px;
  }
  .batch-name {
    position: absolute; top: 360px; left: 0; width: 100%;
    text-align: center;
    font-family: "Barlow", sans-serif; font-weight: 800;
    font-size: 130px; line-height: 1; letter-spacing: 4px;
  }
  .batch-rule {
    position: absolute; top: 503px; left: 81px; width: 616px;
    height: 3px; background: var(--ink);
  }
  .spirit-type {
    position: absolute; top: 520px; left: 0; width: 100%;
    text-align: center; font-size: 33px; letter-spacing: 3px;
  }
  .band-rule {
    position: absolute; left: 0; width: 100%; height: 3px; background: var(--ink);
  }
  .band-rule.top { top: 643px; }
  .band-rule.bottom { top: 701px; }
  .spec {
    position: absolute; top: 654px; font-size: 29px; letter-spacing: 2px;
    width: 200px; text-align: center;
  }
  .spec.abv { left: 73px; }
  .spec.volume { left: 505px; }
  .seal {
    position: absolute; left: 292px; top: 579px; width: 194px; height: 194px;
  }
  .seal text {
    font-family: "Montserrat", sans-serif; font-weight: 700;
    font-size: 12px; letter-spacing: 1px; fill: var(--ink);
  }
</style>
</head>
<body>
<main class="canvas">
  <section class="label">
    <div class="brand-name">SEVEN HERONS</div>
    <div class="brand-rule left"></div>
    <div class="brand-mark"></div>
    <div class="brand-rule right"></div>
    <div class="brand-sub">DISTILLERY</div>

    <h1 class="batch-name">TUBERIX</h1>
    <div class="batch-rule"></div>
    <div class="spirit-type">RUSSIAN POTATO VODKA</div>

    <div class="band-rule top"></div>
    <div class="band-rule bottom"></div>
    <div class="spec abv">40% ALC</div>
    <div class="spec volume">750 ML</div>

    <svg class="seal" viewBox="-97 -97 194 194">
      <defs>
        <path id="seal-top" d="M 0 72 A 72 72 0 1 1 0 -72 A 72 72 0 1 1 0 72"/>
        <path id="seal-bottom" d="M -84 0 A 84 84 0 0 0 84 0"/>
      </defs>
      <circle r="92" fill="var(--label)" stroke="var(--ink)" stroke-width="3"/>
      <circle r="62" fill="none" stroke="var(--ink)" stroke-width="2.5"/>
      <text><textPath href="#seal-top" startOffset="50%" text-anchor="middle">DISTILLED BY SEVEN HERONS DISTILLERY</textPath></text>
      <text><textPath href="#seal-bottom" startOffset="50%" text-anchor="middle">QUEBEC, CANADA</textPath></text>
      <rect x="-40" y="-16" width="80" height="32" rx="14" fill="var(--ink)" role="img" aria-label="Outline map of Lac Vernisse"/>
    </svg>
  </section>
</main>
</body>
</html>
```